GLSW Canberra Pty Ltd

Want something creative and that catches your eye. We are a traffic control companythat offers all aspects of traffic control from planning to roadworks.

Contact Information for Business Card

Dean Vorlick - Director
Ph: 0481 375 206
Email: dean@glsw.com.au
27 Marlow Binks ct Chisholm ACT 2905

```html
<!DOCTYPE html>
<html lang="en">
<head>
<meta charset="utf-8">
<title>GLSW Canberra – Business Card</title>
<link rel="stylesheet" href="https://fonts.googleapis.com/css2?family=Roboto:wght@300;400;500&display=swap">
<style>
  :root {
    --bg: #d9d9d9;
    --card-dark: #2a2a2a;
    --card-light: #ffffff;
    --orange: #e8850f;
    --green: #8cc21a;
    --black: #1c1c1c;
    --ink: #1a1a1a;
    --muted: #9a9a9a;
    --divider: #c8c8c8;
  }
  * { box-sizing: border-box; margin: 0; padding: 0; }
  html, body {
    width: 1200px; height: 900px; overflow: hidden;
    background: var(--bg);
    font-family: "Roboto", Arial, sans-serif;
  }
  .stage { position: relative; width: 1200px; height: 900px; }

  .card {
    position: absolute; left: 250px;
    width: 700px; height: 400px;
    box-shadow: 0 6px 18px rgba(0,0,0,.25);
    overflow: hidden;
  }

  /* Back */
  .card--back { top: 40px; background: var(--card-dark); }
  .services {
    position: absolute; left: 40px; right: 40px; bottom: 52px;
    color: var(--muted); font-size: 11.5px; font-weight: 300;
    line-height: 22px; letter-spacing: .2px;
  }
  .services span + span::before {
    content: "|"; margin: 0 8px; color: #666;
  }
  .back-stripe { position: absolute; left: 0; right: 0; }
  .back-stripe--orange { bottom: 30px; height: 7px; background: var(--orange); }
  .back-stripe--green { bottom: 24px; height: 2px; background: var(--green); }

  /* Front */
  .card--front { top: 470px; background: var(--card-light); }
  .identity {
    position: absolute; left: 56px; top: 26px;
    display: flex; align-items: flex-end;
  }
  .identity__name {
    font-size: 46px; font-weight: 400; color: var(--ink);
    line-height: 1; letter-spacing: .5px; padding-right: 22px;
    border-right: 1px solid var(--divider);
  }
  .identity__role {
    font-size: 20px; font-weight: 500; color: var(--ink);
    padding-left: 22px; padding-bottom: 2px;
  }
  .band {
    position: absolute; left: 0; right: 0;
    display: flex; align-items: center;
    color: #fff; font-size: 15px; font-weight: 300; letter-spacing: .6px;
    padding-left: 40px;
  }
  .band--phone { top: 92px; height: 36px; background: var(--orange); color: #fbe2c4; }
  .band--email { top: 132px; height: 32px; background: var(--green); color: #eef8d8; }
  .band--address { top: 168px; height: 34px; background: var(--black); color: #f2f2f2; }
  .band__label { width: 90px; }
  .band--address .band__label { width: auto; margin-right: 6px; }

  .brand {
    position: absolute; right: 46px; bottom: 46px;
    display: flex; align-items: center; gap: 10px;
  }
  .brand__dot { width: 26px; height: 26px; border-radius: 50%; background: var(--orange); }
  .brand__name { font-size: 26px; font-weight: 500; color: #3a3a3a; letter-spacing: .5px; }
</style>
</head>
<body>
<main class="stage">
  <section class="card card--back" aria-label="Business card back">
    <p class="services">
      <span>Industrial Relations &amp; Employment Accredited for ACT</span><span>Capital Grid Accredited</span><span>Core Power Networks</span><span>Emergency Response Vehicles</span><br>
      <span>24 Hour Service</span><span>TTM Planning &amp; Design for ACT</span><span>Traffic Management Planning &amp; Design</span><span>Traffic Engineering Consultants</span><br>
      <span>Traffic Control</span><span>Territory Roads Accredited</span><span>State Roads Accredited / Council Approval</span><span>Traffic Management Consultants</span><span>C.B.W.U. EBA</span>
    </p>
    <div class="back-stripe back-stripe--orange"></div>
    <div class="back-stripe back-stripe--green"></div>
  </section>

  <section class="card card--front" aria-label="Business card front">
    <div class="identity">
      <h1 class="identity__name">Dean Vorlick</h1>
      <p class="identity__role">Director</p>
    </div>
    <p class="band band--phone"><span class="band__label">Phone</span>: 0481 375 206</p>
    <p class="band band--email"><span class="band__label">Email</span>: dean@glsw.com.au</p>
    <p class="band band--address"><span class="band__label">Address :</span>27 Marlow Binks ct Chisholm ACT 2905</p>
    <div class="brand">
      <span class="brand__dot"></span>
      <span class="brand__name">GLSW Canberra</span>
    </div>
  </section>
</main>
</body>
</html>
```